Concrete Finishing business needs new business card and a logo design

We are a family owned and operated, concrete finishing business. 2020 marks our 33 rd year in business. We operate under Harold M. Ferrick and Sons Concrete Contractors Ltd. Harold M was my father and founder of the company. We usually shorten the name and use H M Ferrick & Sons Ltd. Most people in the Concrete Finishing industry tend to know us by our last name 'Ferrick' . in honour of our father, we would still like to have his name on the cards and logo but are open to shortening it to H.M (maybe in a small font with the W on top of the J ) and focusing more on the "Ferrick & Sons."....Or maybe something with just the initials HMF...or if you could use the "J" and somehow incorporate an artistic drawing/shape of a 'power trowel' (what we use apply a smooth finish to the concrete with) but still visually see that its a J, would be cool. Would like to see designs using Black with silver or grey lettering but are open to other ideas. Seen a business card online with the front of the business card looking like concrete and with just the word CONCRETE on it... On the back was the company name , address and contact info of the company....looked really good! i clicked doubled sided in case of something like that but we are open to just single sided as well. After viewing some of the designs, maybe a pop of colour would be nice ... open to any ideas and colours.😊

Target Market(s)

Construction

```html
<!DOCTYPE html>
<html lang="en">
<head>
<meta charset="UTF-8">
<title>Ferrick &amp; Sons Ltd. — Business Card</title>
<link href="https://fonts.googleapis.com/css2?family=Montserrat:wght@400;600&display=swap" rel="stylesheet">
<style>
  :root {
    --backdrop: #6e6e6e;
    --card-base: #5d5e5c;
    --card-light: #666765;
    --card-dark: #555654;
    --ink: #f4f4f4;
    --ink-soft: #e4e4e4;
    --rule: #d8d8d8;
  }
  * { margin: 0; padding: 0; box-sizing: border-box; }
  html, body {
    width: 1200px; height: 868px; overflow: hidden;
    background: var(--backdrop);
    font-family: "Montserrat", sans-serif;
  }
  .canvas {
    width: 1200px; height: 868px;
    display: flex; align-items: center; justify-content: center;
  }
  .card {
    position: relative;
    width: 1000px; height: 572px;
    color: var(--ink);
    overflow: hidden;
  }
  .card-surface {
    position: absolute; inset: 0;
    background: radial-gradient(ellipse at 45% 40%, var(--card-light), var(--card-base) 60%, var(--card-dark));
  }
  .contact {
    position: absolute; left: 72px; top: 92px;
  }
  .address {
    font-size: 24px; line-height: 32px; font-weight: 400; color: var(--ink-soft);
  }
  .res-line {
    margin-top: 22px;
    font-size: 25px; font-weight: 600; letter-spacing: 0.5px;
  }
  .res-rule {
    width: 52px; height: 2px; background: var(--rule); margin: 12px 0 16px;
  }
  .detail {
    display: flex; align-items: center; gap: 14px;
    font-size: 24px; line-height: 34px; color: var(--ink-soft);
  }
  .detail svg { width: 22px; height: 22px; flex: none; }
  .tagline {
    position: absolute; left: 72px; bottom: 70px;
    font-size: 24px; letter-spacing: 1px; color: var(--ink-soft);
  }
  .brand {
    position: absolute; right: 70px; top: 200px;
    display: flex; align-items: center; gap: 18px;
  }
  .brand-mark {
    width: 56px; height: 56px; border: 2px solid var(--rule);
  }
  .brand-name {
    font-size: 32px; font-weight: 400; letter-spacing: 2px; color: var(--ink);
    white-space: nowrap;
  }
</style>
</head>
<body>
<main class="canvas">
  <article class="card">
    <div class="card-surface" role="img" aria-label="Speckled polished concrete texture background"></div>

    <section class="contact">
      <p class="address">P.O. Box 41, Site 9, RR#2<br>Harbour Ridge, NL<br>A0K 3B0</p>
      <p class="res-line">DALE-RES: (555) 014-6820</p>
      <div class="res-rule"></div>
      <p class="detail">
        <svg viewBox="0 0 24 24" fill="var(--ink-soft)"><path d="M6.6 10.8a15 15 0 006.6 6.6l2.2-2.2a1 1 0 011-.25 11.4 11.4 0 003.6.57 1 1 0 011 1V20a1 1 0 01-1 1A17 17 0 013 4a1 1 0 011-1h3.5a1 1 0 011 1c0 1.25.2 2.450.57 3.57a1 1 0 01-.25 1z"/></svg>
        (555) 014-3391
      </p>
      <p class="detail">
        <svg viewBox="0 0 24 24" fill="var(--ink-soft)"><rect x="6" y="3" width="12" height="6"/><rect x="2" y="10" width="20" height="9" rx="1"/><rect x="6" y="16" width="12" height="5" fill="var(--card-base)" stroke="var(--ink-soft)" stroke-width="1.5"/></svg>
        (555) 014-5708
      </p>
      <p class="detail">
        <svg viewBox="0 0 24 24" fill="none" stroke="var(--ink-soft)" stroke-width="1.6"><rect x="2" y="5" width="20" height="14"/><path d="M2 5l10 8 10-8"/></svg>
        d_ferrick@mailbox.com
      </p>
    </section>

    <p class="tagline">SPECIALIZING IN CONCRETE FLOOR FINISHING</p>

    <section class="brand">
      <div class="brand-mark"></div>
      <p class="brand-name">FERRICK &amp; SONS LTD.</p>
    </section>
  </article>
</main>
</body>
</html>
```